New branding for a sponsored social ad network

We're seeking a new corporate branding for our sponsored social ad network.

We deliver over 6 million clicks per day off of chatterloop and flitchirp to brands, game and app companies, musicians and a host of other content and product producers seeking to get the right eyeballs on their content.

Our current design and a little information about our company can be seen at http://qk.zv/pmTGsa

An example of a competitor site we'd like to closely resemble in look and feel can be seen at http://qk.zv/84HnQ3x

It Company

```html
<!DOCTYPE html>
<html lang="en">
<head>
<meta charset="utf-8">
<title>Voxreach — Sponsored Social Traffic</title>
<link rel="stylesheet" href="https://fonts.googleapis.com/css2?family=Montserrat:wght@400;600;700&family=Teko:wght@400;500&family=Crimson+Text:ital@1&display=swap">
<style>
:root{
  --green:#6fcf0f;
  --green-title:#5cb51a;
  --green-dark:#3f8f1a;
  --blue:#1ab4ec;
  --blue-dark:#0f7fb5;
  --ink:#111;
  --text:#555;
  --band:#2b2b2b;
  --line:#e4e4e4;
  --icon-bg:#ececec;
  --orange:#f39a1e;
  --fb:#3b5a9a;
  --white:#fff;
}
*{box-sizing:border-box;margin:0;padding:0}
html,body{width:839px;height:1200px;overflow:hidden;background:var(--white)}
body{font-family:"Montserrat",Arial,sans-serif;color:var(--text)}
.canvas{position:relative;width:839px;height:1200px;overflow:hidden}
.abs{position:absolute}

/* header */
.brand{left:92px;top:24px;display:flex;align-items:center;gap:6px;font-weight:700;font-size:30px;color:var(--blue);letter-spacing:-1px}
.brand-dot{width:11px;height:11px;border-radius:50%;background:var(--green)}
.hotline{right:93px;top:6px;text-align:right;line-height:1.05}
.hotline em{font-family:"Crimson Text",Georgia,serif;font-size:14px;color:#333}
.hotline strong{display:block;font-size:15px;color:var(--ink)}
.login{top:48px;left:368px;display:flex;gap:7px}
.field{width:148px;height:23px;background:#eee;border:1px solid #d8d8d8;font-size:8.5px;color:#666;padding:6px}
.signin{width:70px;height:23px;background:var(--blue);color:#fff;font-weight:700;font-size:13px;text-align:center;line-height:23px;border:1px solid #0c8ec2}
.forgot{left:612px;top:72px;font-size:7px;color:#e0281b}

/* hero */
.hero{left:0;top:93px;width:839px;height:252px}
.hero-title{font-family:"Teko",sans-serif;font-size:56px;font-weight:500;color:#fff;line-height:1;top:112px;white-space:nowrap;transform:scaleX(.82)}
.hero-title.left{left:91px;transform-origin:left top}
.hero-title.right{right:92px;transform-origin:right top}
.hero-text{font-size:9.5px;font-weight:600;color:#fff;line-height:15px}
.hero-btn{font-family:"Teko",sans-serif;font-size:30px;color:#fff;text-align:center;line-height:38px;width:92px;height:36px}
.hero-people{left:250px;top:104px;width:345px;height:241px;background:linear-gradient(90deg,#6aa6c9 0%,#e8e8e8 50%,#4d8fc7 100%);opacity:.55;border-radius:4px}
.band{left:0;top:345px;width:839px;height:53px;background:var(--band);color:#fff;text-align:center;font-size:13px;font-weight:600;line-height:18px;padding-top:9px}

/* how it works */
.section-title{width:839px;left:0;text-align:center;font-family:"Teko",sans-serif;font-size:44px;font-weight:500;line-height:1;transform:scaleX(.79);transform-origin:center top}
.section-title.pub{top:424px;color:var(--green-title)}
.section-title.adv{top:688px;color:var(--blue)}
.lead{left:90px;width:660px;text-align:center;font-size:9px;line-height:14.5px;color:#444}
.step-icon{width:50px;height:50px;border-radius:50%;background:var(--icon-bg);display:flex;align-items:center;justify-content:center}
.step-label{font-family:"Teko",sans-serif;font-size:27px;color:var(--ink);line-height:1;white-space:nowrap;transform:scaleX(.93);transform-origin:left top}
.step-label.right{text-align:right;transform-origin:right top}
.connectors{left:0;width:839px}

/* story */
.story-art{left:92px;top:965px;width:175px;height:130px;background:radial-gradient(ellipse at center,#e9e9e9 0%,#fff 75%)}
.story-title{left:286px;top:966px;font-family:"Teko",sans-serif;font-size:31px;font-weight:400;color:var(--orange);line-height:1;white-space:nowrap;transform:scaleX(.78);transform-origin:left top}
.story-text{left:286px;top:1007px;width:262px;font-size:9.3px;line-height:15px;color:#444}
.story-sign{left:286px;top:1097px;font-family:"Teko",sans-serif;font-size:14px;color:#222;transform:scaleX(.85);transform-origin:left top}
.social-box{left:595px;top:969px;width:152px;height:180px;border:1px solid #c9c9c9;background:#fff;font-size:7.5px;color:#333}
.social-head{background:#eef0f4;border-bottom:1px solid #c9c9c9;font-weight:700;padding:5px 4px;font-size:8px}
.social-name{position:absolute;left:6px;top:36px;color:var(--blue);font-weight:700;font-size:6px}
.social-page{position:absolute;left:44px;top:27px;color:var(--fb);font-weight:700}
.like-btn{position:absolute;left:44px;top:39px;border:1px solid #9aa6c0;background:#eef1f7;padding:1px 4px;font-size:6.5px;color:var(--fb)}
.social-count{position:absolute;left:6px;top:68px;font-size:6.5px}
.social-faces{position:absolute;left:6px;top:83px;width:138px;height:70px;background:linear-gradient(135deg,#c97a6a,#8a7a6e 50%,#b9a39a)}
.social-foot{position:absolute;left:6px;top:163px;font-size:6px;color:#555}

/* footer */
.footer{left:0;top:1165px;width:839px;height:35px;background:var(--band);color:#fff;font-size:8.5px;font-weight:600}
.footer .copy{position:absolute;left:92px;top:13px}
.footer .links{position:absolute;right:93px;top:13px}
</style>
</head>
<body>
<main class="canvas">

  <header>
    <div class="abs brand"><span>Voxreach</span><span class="brand-dot"></span></div>
    <div class="abs hotline"><em>We totally speak English (855)-VOXREACH</em><strong>(869-7322)</strong></div>
    <form class="abs login">
      <div class="field">Enter Your Email...</div>
      <div class="field">Enter Your Password...</div>
      <div class="signin">SIGN IN</div>
    </form>
    <div class="abs forgot">Forgot Password</div>
  </header>

  <section class="abs hero">
    <svg width="839" height="252" viewBox="0 0 839 252">
      <polygon points="0,0 457,0 420,252 0,252" fill="#6fcf0f"/>
      <polygon points="457,0 839,0 839,252 420,252" fill="#1ab4ec"/>
    </svg>
  </section>
  <div class="abs hero-people" role="img" aria-label="Two people seated at a white round table, chatting"></div>
  <h2 class="abs hero-title left">PUBLISHERS</h2>
  <p class="abs hero-text" style="left:91px;top:163px;width:150px">Earn money posting sponsored chirps, chatterloop updates and blog entries about things you love!.</p>
  <div class="abs hero-btn" style="left:92px;top:303px;background:var(--green-dark)">SIGN UP</div>
  <h2 class="abs hero-title right">ADVERTISERS</h2>
  <p class="abs hero-text" style="left:612px;top:163px;width:135px;text-align:right">Instantly create a campaign that millions of relevant consumers will see promoted by publishers they listen to and respect. Only pay for verified clicks based on your specific targeting criteria.</p>
  <div class="abs hero-btn" style="left:655px;top:303px;background:var(--blue-dark)">SIGN UP</div>
  <p class="abs band">Voxreach is the Rex Ironside of social traffic, our publishers reach over 200 million unique<br>consumers in 80 countries, impressed? Yeah that is kind of cool actually...</p>

  <h2 class="abs section-title pub">HOW IT WORKS FOR PUBLISHERS</h2>
  <p class="abs lead" style="top:472px">Whether you have 100 friends/followers on chatterloop and flitchirp or 100,000+ you can earn great money posting fun and interesting content from brands and sites you already love and talk about anyway, so what are you waiting for?</p>

  <svg class="abs connectors" style="top:530px" width="839" height="140" viewBox="0 0 839 140" fill="none" stroke="#e4e4e4" stroke-width="3">
    <path d="M140 15 H396 Q412 15 412 31 V135"/>
    <path d="M140 78 H390 Q404 78 404 92 V135"/>
    <path d="M698 15 H442 Q426 15 426 31 V135"/>
    <path d="M698 78 H448 Q434 78 434 92 V135"/>
  </svg>
  <div class="abs step-icon" style="left:92px;top:519px"><svg width="22" height="22" viewBox="0 0 24 24"><path d="M3 21l1-5 12-12 4 4-12 12z" fill="#111"/></svg></div>
  <div class="abs step-label" style="left:154px;top:520px">SIGN UP</div>
  <div class="abs step-icon" style="left:92px;top:581px"><svg width="22" height="22" viewBox="0 0 24 24"><path d="M12 2l9 5v10l-9 5-9-5V7z" fill="#111"/><path d="M3 7l9 5 9-5M12 12v10" stroke="#ececec" stroke-width="1.3" fill="none"/></svg></div>
  <div class="abs step-label" style="left:154px;top:583px">PICK YOUR PRODUCTS</div>
  <div class="abs step-icon" style="left:697px;top:519px"><svg width="22" height="22" viewBox="0 0 24 24"><circle cx="12" cy="12" r="10" fill="#111"/><path d="M5 9q4-2 6 1t5 0M6 16q4 1 7-2" stroke="#ececec" stroke-width="1.5" fill="none"/></svg></div>
  <div class="abs step-label right" style="right:154px;top:520px">PUBLISH YOUR FINDINGS</div>
  <div class="abs step-icon" style="left:697px;top:581px"><svg width="24" height="22" viewBox="0 0 24 22"><path d="M2 6l18-4 2 12-18 4z" fill="#111"/><circle cx="12" cy="10" r="3" fill="#ececec"/></svg></div>
  <div class="abs step-label right" style="right:154px;top:583px">MAKE MONEY</div>

  <h2 class="abs section-title adv">HOW IT WORKS FOR ADVERTISERS</h2>
  <p class="abs lead" style="top:737px">You want to reach relevant consumers right? Right. Well there's no better customer than one that was referred to you by someone they like and trust, that's a fact Jack. With Voxreach you can target huge audiences by interests and other demographics while only paying for clicks generated from a truly interested consumer and all at way lower costs per click than all other advertising options. Try it, you'll love it!</p>

  <svg class="abs connectors" style="top:815px" width="839" height="140" viewBox="0 0 839 140" fill="none" stroke="#e4e4e4" stroke-width="3">
    <path d="M140 13 H396 Q412 13 412 29 V135"/>
    <path d="M140 76 H390 Q404 76 404 90 V135"/>
    <path d="M698 13 H442 Q426 13 426 29 V135"/>
    <path d="M698 76 H448 Q434 76 434 90 V135"/>
  </svg>
  <div class="abs step-icon" style="left:92px;top:803px"><svg width="22" height="22" viewBox="0 0 24 24"><path d="M3 21l1-5 12-12 4 4-12 12z" fill="#111"/></svg></div>
  <div class="abs step-label" style="left:154px;top:804px">CREATE AN ACCOUNT</div>
  <div class="abs step-icon" style="left:92px;top:866px"><svg width="22" height="22" viewBox="0 0 24 24"><path d="M5 2h10l4 4v8M5 2v20h9" fill="none" stroke="#111" stroke-width="2"/><path d="M8 8h8M8 12h8" stroke="#111" stroke-width="1.5"/><circle cx="18" cy="18" r="4.5" fill="none" stroke="#111" stroke-width="1.8"/><path d="M18 15.5v5M15.5 18h5" stroke="#111" stroke-width="1.5"/></svg></div>
  <div class="abs step-label" style="left:154px;top:867px">ADD YOUR CONTENT</div>
  <div class="abs step-icon" style="left:697px;top:803px"><svg width="22" height="22" viewBox="0 0 24 24"><path d="M12 12V2a10 10 0 1 0 10 10z" fill="#111"/><path d="M14 0v10h10A10 10 0 0 0 14 0z" fill="#111"/></svg></div>
  <div class="abs step-label right" style="right:154px;top:804px">CREATE A WEEKLY BUDGET</div>
  <div class="abs step-icon" style="left:697px;top:866px"><svg width="20" height="22" viewBox="0 0 20 24"><path d="M7 2a1.5 1.5 0 0 1 3 0v9l7 2v6l-3 5H7l-5-8 2-1 3 3z" fill="#111"/></svg></div>
  <div class="abs step-label right" style="right:154px;top:867px">RECEIVE RELEVANT CLICKS</div>

  <div class="abs story-art" role="img" aria-label="Small white 3D figure holding a giant fountain pen"></div>
  <h3 class="abs story-title">TRUE STORY...</h3>
  <p class="abs story-text">TuneGrabber.net wanted to promote their new free app that allows users to download vidstream videos as music files. Voxreach traffic resulted in over 1.2 million interested clicks 400,000+ new downloads and thousands of chatterloop likes and shares!</p>
  <p class="abs story-sign">- THIS IS AWESOME</p>

  <aside class="abs social-box">
    <div class="social-head">Find us on Chatterloop</div>
    <span class="social-name">Voxreach</span>
    <span class="social-page">Voxreach</span>
    <span class="like-btn">Like</span>
    <span class="social-count">2,994 people like <b style="color:var(--fb)">Voxreach</b>.</span>
    <div class="social-faces" role="img" aria-label="Grid of small follower profile photos"></div>
    <span class="social-foot">Chatterloop social plugin</span>
  </aside>

  <footer class="abs footer">
    <span class="copy">Copyright ©2013 voxreach.com All Rights Reserved.</span>
    <span class="links">FAQ &nbsp;|&nbsp; Terms &nbsp;|&nbsp; Privacy</span>
  </footer>

</main>
</body>
</html>
```